Design refresh required for educational resources

A full redesign/refresh is required for an education resource kit.
The final outputs will include:
- Powerpoint slide template
- parent handout template
- overview template
- 2 different types of lesson plan templates (can be related but need to have some differences to distinguish between the two)
- 2 x branded labels for resources
- teacher 'intervention plan' summary sheet
- 'scope and sequence' document
Design needs to have a fun, modern feel, capturing elements of the New Zealand landscape, flora and/or fauna.
The resources will be used as part of a teaching kit for use in schools.
Please see attached files for existing samples of some of the above documents. Full content to be provided for successful applicant.
Please submit sample of one or two of the documents to bid for this work - enough so that I can see the overall design aesthetic you are proposing.
New Zealand teachers and parents of 5 year old children

```html
<!DOCTYPE html>
<html lang="en">
<head>
<meta charset="utf-8">
<title>Week 2 – Overview and Lesson 1</title>
<link href="https://fonts.googleapis.com/css2?family=Montserrat:wght@300;500;600&family=Lexend:wght@300;400;500&display=swap" rel="stylesheet">
<style>
  :root {
    --stage: #d4d4d4;
    --paper: #ffffff;
    --leaf: #6fa93f;
    --leaf-line: #a9cc8a;
    --berry: #6a0f2f;
    --berry-soft: #efe3e7;
    --ink: #1d1b1c;
    --photo-dark: #3b3524;
    --photo-mid: #6f6438;
    --photo-light: #a3903f;
  }
  * { box-sizing: border-box; margin: 0; padding: 0; }
  html, body { width: 1200px; height: 1200px; overflow: hidden; }
  body {
    background: var(--stage);
    font-family: "Lexend", sans-serif;
    color: var(--ink);
    position: relative;
  }
  .page {
    position: absolute;
    width: 645px;
    height: 912px;
    overflow: hidden;
  }
  .page--overview { left: 108px; top: 194px; background: var(--paper); }
  .page--lesson { left: 481px; top: 93px; background: var(--berry-soft); }

  .week-label {
    position: absolute; left: 62px; top: 48px;
    font-family: "Montserrat", sans-serif; font-weight: 600;
    font-size: 14px; letter-spacing: 8px;
  }
  .week-number {
    position: absolute; left: 62px; top: 70px;
    width: 74px; height: 83px;
    display: flex; align-items: center; justify-content: center;
    font-family: "Montserrat", sans-serif; font-weight: 600;
    font-size: 50px; color: #fff;
  }
  .page--overview .week-label { color: var(--leaf); }
  .page--overview .week-number { background: var(--leaf); }
  .page--lesson .week-label { color: #fff; }
  .page--lesson .week-number { background: var(--berry); }

  .overview-title {
    position: absolute; left: 62px; top: 186px;
    font-family: "Montserrat", sans-serif; font-weight: 600;
    font-size: 22px; letter-spacing: 6px; color: var(--leaf);
  }
  .overview-table {
    position: absolute; left: 62px; top: 244px; width: 520px;
  }
  .overview-row {
    display: grid; grid-template-columns: 179px 1fr;
    border-top: 1px dotted var(--leaf-line);
    padding: 12px 0 12px;
  }
  .overview-row:last-child { border-bottom: 1px dotted var(--leaf-line); padding-bottom: 14px; }
  .row-label {
    font-family: "Montserrat", sans-serif; font-weight: 600;
    font-size: 10.5px; letter-spacing: 1.6px; color: var(--leaf);
    line-height: 1.5; text-transform: uppercase; padding-top: 2px;
  }
  .row-value { font-size: 13px; line-height: 16px; }
  .row-value strong { font-weight: 500; }
  .chips { display: flex; flex-wrap: wrap; gap: 6px 6px; align-items: center; }
  .chip {
    display: inline-block; padding: 2px 6px;
    border: 1px solid var(--leaf-line); border-radius: 3px;
    font-size: 14.5px; line-height: 19px; font-weight: 500; background: #fff;
  }
  .chip span { font-weight: 300; }
  .plain { font-size: 14.5px; }
  .materials { list-style: none; }
  .materials li { position: relative; padding-left: 16px; margin-bottom: 8px; line-height: 15px; }
  .materials li:last-child { margin-bottom: 0; }
  .materials li::before {
    content: ""; position: absolute; left: 1px; top: 6px;
    width: 4px; height: 4px; border-radius: 50%; background: var(--leaf);
  }

  .lesson-hero {
    position: absolute; left: 0; top: 0; width: 645px; height: 323px;
    background: linear-gradient(170deg, #5b5a55 0%, var(--photo-dark) 30%, var(--photo-mid) 62%, var(--photo-light) 100%);
  }
  .lesson-hero__band {
    position: absolute; left: 0; top: 323px; width: 645px; height: 8px;
    background: var(--berry);
  }
  .lesson-title {
    position: absolute; left: 62px; top: 210px;
    font-family: "Montserrat", sans-serif; font-weight: 300;
    font-size: 52px; color: #fff; letter-spacing: 1px;
  }
  .lesson-body { position: absolute; left: 62px; top: 374px; width: 560px; }
  .section-label {
    font-family: "Montserrat", sans-serif; font-weight: 600;
    font-size: 10.5px; letter-spacing: 1.8px; color: var(--berry);
    text-transform: uppercase; margin-bottom: 10px;
  }
  .book-title { font-weight: 500; font-size: 17px; line-height: 1.4; }
  .book-author { font-weight: 300; font-size: 17px; line-height: 1.4; }
  .lesson-section { margin-bottom: 29px; }
  .lesson-section--book { margin-bottom: 59px; }
  .page--lesson .chip { border-color: var(--berry); background: transparent; }
  .page--lesson .chips { gap: 6px 6px; }
</style>
</head>
<body>

<section class="page page--overview">
  <div class="week-label">WEEK</div>
  <div class="week-number">2</div>
  <h1 class="overview-title">OVERVIEW</h1>
  <div class="overview-table">
    <div class="overview-row">
      <div class="row-label">Book</div>
      <div class="row-value"><strong>The Moonlit Wanderings of Ruru and Kiwi</strong><br>by Hana Moretti and Jo Tamsin</div>
    </div>
    <div class="overview-row">
      <div class="row-label">Vocabulary<br>target words</div>
      <div class="row-value chips">
        <span class="chip">velvety</span><span class="chip">decorate</span><span class="chip">marama <span>(moon)</span></span>
        <span class="chip">rākau <span>(tree)</span></span>
      </div>
    </div>
    <div class="overview-row">
      <div class="row-label">Target phonemes<br>and graphemes</div>
      <div class="row-value chips">
        <span class="chip">M</span><span class="chip">m</span><span class="plain">and</span><span class="chip">D</span><span class="chip">d</span>
      </div>
    </div>
    <div class="overview-row">
      <div class="row-label">Target picture<br>card words</div>
      <div class="row-value chips">
        <span class="chip">dog</span><span class="chip">dam</span><span class="chip">dot</span><span class="chip">den</span><span class="chip">dig</span>
        <span class="chip">map</span><span class="chip">men</span><span class="chip">mud</span><span class="chip">mat</span>
      </div>
    </div>
    <div class="overview-row">
      <div class="row-label">Readers</div>
      <div class="row-value">CV CVC VC words with m and d<br>Easier: Mud Map; Dad and Me<br>Harder: Meg and the Damp Den</div>
    </div>
    <div class="overview-row">
      <div class="row-label">Materials<br>for games</div>
      <div class="row-value">
        <ul class="materials">
          <li>Large d and m letter cards, lower and upper case</li>
          <li>Target picture cards: picture on one side, word reverse</li>
          <li>Segmentation board and counters</li>
          <li>‘Special container’ for the phoneme identity game</li>
          <li>White board and markers</li>
        </ul>
      </div>
    </div>
  </div>
</section>

<section class="page page--lesson">
  <div class="lesson-hero" role="img" aria-label="Photograph of a New Zealand mountain valley with golden tussock, a waterfall and a small tarn"></div>
  <div class="lesson-hero__band"></div>
  <div class="week-label">WEEK</div>
  <div class="week-number">2</div>
  <h1 class="lesson-title">LESSON 1</h1>

  <div class="lesson-body">
    <div class="lesson-section lesson-section--book">
      <div class="section-label">Book</div>
      <div class="book-title">The Moonlit Wanderings of Ruru and Kiwi</div>
      <div class="book-author">by Hana Moretti and Jo Tamsin</div>
    </div>
    <div class="lesson-section">
      <div class="section-label">Vocabulary target words</div>
      <div class="chips">
        <span class="chip">velvety</span><span class="chip">decorate</span><span class="chip">rākau <span>(tree)</span></span><span class="chip">marama <span>(moon)</span></span>
      </div>
    </div>
    <div class="lesson-section">
      <div class="section-label">Target phonemes and graphemes</div>
      <div class="chips">
        <span class="chip">M</span><span class="chip">m</span><span class="plain">and</span><span class="chip">D</span><span class="chip">d</span>
      </div>
    </div>
    <div class="lesson-section">
      <div class="section-label">Target picture card words (English)</div>
      <div class="chips">
        <span class="chip">dog</span><span class="chip">dam</span><span class="chip">dot</span><span class="chip">den</span><span class="chip">dig</span><span class="chip">mat</span><span class="chip">mop</span><span class="chip">map</span><span class="chip">men</span><span class="chip">mud</span>
      </div>
    </div>
    <div class="lesson-section">
      <div class="section-label">Target picture card words (English)</div>
      <div class="chips">
        <span class="chip">marama</span><span class="chip">manu</span><span class="chip">moe</span>
      </div>
    </div>
  </div>
</section>

</body>
</html>
```